hostels chain website in Barcelona

We need a web design for a brand of youth hostels located in Barcelona called El Nido de Mirenca. We have two hostels with different location. We offer cheap accomodation in shared dorms for young people (avg. 23 years old), but we aim to arrive to cultural tourist more than party people. We offer a local experience by hiring only local staff and by doing some free activities related to Barcelona.
Updates

Hello, In our website it has to appear the number and logo of the official agency that approve the bussiness. It is in our website, it is an orange box with the number 731 and 249. Besides this, we also like to have the voyagenote box where it is possible to read reviews. Regards Montserrat

Target Market(s)

Young people between 18 to 35 years old, that loves travelling and living new experiences.

Industry/Entity Type

Tourist

Font styles to use
Other font styles liked:
• Gladifilthefte and Rockwell

Requirements
Must have
• Pictures of the hostel, booking buttom, groups section and activities section.
It must talk about two different locations.
Colors and design has to be related to the decoration of the hostel and the logo.
Nice to have
• It has to show happiness and cleanliness. we like the website http://www.posadalunetabcn.com/ as a reference.
Should not have
• Boring things

```html
<!DOCTYPE html>
<html lang="en">
<head>
<meta charset="utf-8">
<title>El Nido de Mirenca Hostel</title>
<link href="https://fonts.googleapis.com/css2?family=Arvo:wght@400;700&family=Open+Sans:wght@400;700&display=swap" rel="stylesheet">
<style>
:root{
  --navy:#0d4f7a;
  --teal:#008b84;
  --red:#ee3e34;
  --text:#9a9a9a;
  --dark:#3a3a3a;
  --footer:#333333;
  --line:#d6d6d6;
  --white:#ffffff;
}
*{margin:0;padding:0;box-sizing:border-box}
html,body{width:778px;height:1200px;overflow:hidden;background:var(--white)}
body{position:relative;font-family:"Arvo",serif;color:var(--text)}
.abs{position:absolute}
.brand{left:117px;top:40px;display:flex;align-items:center;gap:8px}
.brand-dot{width:22px;height:22px;border-radius:50%;background:var(--navy)}
.brand-name{font-family:"Arvo",serif;font-size:21px;font-weight:700;color:var(--navy);line-height:1}
.book-btn{left:606px;top:60px;width:56px;height:22px;background:var(--navy);color:var(--white);border-radius:3px;font-family:"Open Sans",sans-serif;font-weight:700;font-size:8px;display:flex;align-items:center;justify-content:center}
.main-nav{left:369px;top:101px;display:flex;gap:24px;font-size:8.5px;color:#333;text-transform:uppercase}
.main-nav .active{color:var(--navy);border-bottom:1.5px solid var(--navy);padding-bottom:3px}
.hero{left:117px;top:138px;width:545px;height:268px;background:linear-gradient(180deg,#a9cfe8 0%,#d9e3e5 25%,#b98a5d 55%,#7c8f4a 80%,#5c6b3a 100%)}
.dots{left:371px;top:420px;display:flex;gap:3px}
.dots span{width:3px;height:3px;border-radius:50%;background:#888}
.dots span:first-child{background:#333}
.h2{font-size:13.5px;color:var(--navy);font-weight:400}
.body-text{font-size:8.3px;line-height:13.5px;color:var(--text)}
.read-btn{width:58px;height:27px;border:1px solid var(--line);border-radius:3px;background:#f7f7f7;font-family:"Open Sans",sans-serif;font-weight:700;font-size:8px;color:#555;display:flex;align-items:center;justify-content:center}
.thumb{width:79px;height:62px}
.band{top:653px;height:121px;color:var(--white);padding:20px 22px}
.band h3{font-size:13px;font-weight:700;margin-bottom:12px}
.band p{font-family:"Open Sans",sans-serif;font-size:6.8px;line-height:10.5px;margin-bottom:14px}
.band .detail-btn{display:inline-block;border:1px solid var(--white);border-radius:2px;font-family:"Open Sans",sans-serif;font-size:7px;padding:6px 8px}
.activity-card{left:469px;top:996px;width:193px;height:93px;background:var(--dark);padding:14px 11px;color:var(--white)}
.activity-card h4{font-size:12.5px;font-weight:400;line-height:15px;margin-bottom:8px}
.activity-card p{font-size:7.4px;line-height:11px;color:#aaa}
.footer{left:0;top:1122px;width:778px;height:78px;background:var(--footer)}
.footer-nav{left:116px;top:1152px;display:flex;gap:24px;font-size:8px;color:var(--white);text-transform:uppercase}
.copyright{left:116px;top:1168px;font-size:5.5px;color:var(--white);font-weight:700}
.social{left:544px;top:1154px;display:flex;gap:12px}
.social span{width:21px;height:21px;border-radius:2px}
</style>
</head>
<body>
  <div class="abs brand"><span class="brand-dot"></span><span class="brand-name">El Nido de Mirenca</span></div>
  <div class="abs book-btn">BOOK NOW</div>
  <nav class="abs main-nav">
    <span class="active">Home</span><span>The Hostel</span><span>Events</span><span>Contact</span><span>Gallery</span>
  </nav>

  <div class="abs hero" role="img" aria-label="Panoramic view of Barcelona from a mosaic-decorated park"></div>
  <div class="abs dots"><span></span><span></span><span></span><span></span><span></span><span></span></div>

  <h2 class="abs h2" style="left:117px;top:461px">About us</h2>
  <div class="abs body-text" style="left:117px;top:488px;width:335px">
    <p>Lorem ipsum dolor sit amet, consectetur adipiscing elit, sed do eiusmod tempor incididunt ut labore et dolore magna aliqua. Ut enim ad minim veniam, quis nostrud exercitation ullamco laboris nisi ut aliquip ex ea commodo consequat.</p>
    <p style="margin-top:13px">Duis aute irure dolor in reprehenderit in voluptate velit esse cillum dolore eu fugiat nulla pariatur. Excepteur sint occaecat cupidatat non proident, sunt in culpa qui officia deserunt mollit anim id est laborum.</p>
  </div>
  <div class="abs read-btn" style="left:117px;top:598px">Read More</div>

  <h2 class="abs h2" style="left:498px;top:461px">Photo Gallery</h2>
  <div class="abs thumb" style="left:498px;top:492px;background:linear-gradient(180deg,#eeeeec,#c9c6c0)" role="img" aria-label="Hostel lounge with grey sofa"></div>
  <div class="abs thumb" style="left:582px;top:492px;background:linear-gradient(135deg,#3f6a92,#567ea6)" role="img" aria-label="Blue painted wall with yellow lettering"></div>
  <div class="abs thumb" style="left:498px;top:561px;background:linear-gradient(180deg,#e6e3dc,#b8b4aa)" role="img" aria-label="Close-up of a white lamp"></div>
  <div class="abs thumb" style="left:582px;top:561px;background:linear-gradient(135deg,#b96b5c,#7a8f5c)" role="img" aria-label="Red lockers beside green plants"></div>

  <div class="abs band" style="left:117px;width:272px;background:var(--teal)">
    <h3>Parc del Turó Location</h3>
    <p>Set in a townhouse built in 1925 on the site of a former monastery, it was completely renovated in 2013</p>
    <span class="detail-btn">View Details</span>
  </div>
  <div class="abs band" style="left:389px;width:273px;background:var(--red)">
    <h3>Casa Verdera Location</h3>
    <p>Set in a townhouse built in 1925 on the site of a former monastery, it was completely renovated in 2013</p>
    <span class="detail-btn">View Details</span>
  </div>

  <h2 class="abs h2" style="left:117px;top:826px">Groups staying in El Nido de Mirenca hostels</h2>
  <div class="abs" style="left:117px;top:860px;width:329px;height:126px;background:linear-gradient(180deg,#e8e4da 0%,#c9a57a 45%,#8a5a4a 100%)" role="img" aria-label="Group of young guests sitting together in the hostel lounge"></div>
  <p class="abs body-text" style="left:117px;top:1006px;width:335px">At El Nido de Mirenca we love receiving groups. Come and find everything that you may need for your trip, with excellent services and facilities. We have hosted all kind of groups: schools, cultural, sports.</p>
  <div class="abs read-btn" style="left:117px;top:1065px">Read More</div>

  <h2 class="abs h2" style="left:469px;top:826px">Free&nbsp; Activities</h2>
  <div class="abs" style="left:469px;top:860px;width:193px;height:136px;background:linear-gradient(180deg,#8c8274 0%,#6b6359 55%,#4a4442 100%)" role="img" aria-label="Group of travellers on a walking tour in front of a stone building"></div>
  <div class="abs activity-card">
    <h4>FREE ACTIVITIES<br>for our customers !</h4>
    <p>Free walking tour in the gothic district of Barcelona every Saturday morning</p>
  </div>

  <footer class="abs footer"></footer>
  <nav class="abs footer-nav"><span>Home</span><span>The Hostel</span><span>Events</span><span>Contact</span><span>Gallery</span></nav>
  <div class="abs copyright">© 2014 ALL RIGHTS RESERVED</div>
  <div class="abs social">
    <span style="background:#f5a623"></span>
    <span style="background:#5fb4e6"></span>
    <span style="background:#e27aa6"></span>
    <span style="background:#3b5b9a"></span>
  </div>
</body>
</html>
```